High-End Print/Digital Ad for Unique Luxury Travel Company Required

Objective:
Design a compelling and visually striking advertisement that highlights our company’s unmatched luxury travel experiences. The ad should elevate our brand image, spark curiosity, and drive prospective clients to contact us.
Target Audience:
• Affluent individuals seeking extraordinary, tailor-made travel experiences
• Affluent, luxury, high-net-worth individuals looking for value, expertise, and white-glove service
• Professionals or retirees who appreciate unique, thoughtfully curated travel over mainstream tourism
Key Messages to Communicate:
• One-of-a-kind luxury travel: Once-in-a-lifetime experiences that are curated with creativity and meticulous attention to detail
• Exceptional service: White-glove, personalized planning from start to finish
• 38 years’ travel experience – expert knowledge of destinations, modes of travel, premium accommodations and well-established, meaningful industry connections.
• Highly trusted: Cruise line executives often say, “No one does what you do.”
Tone and Style:
• Elegant, luxurious, sophisticated
• Eye-catching, polished, and modern
• Professional but warm—conveys trust and credibility
• High-impact visuals (full-bleed imagery, custom graphics, or high-end photography)
Deliverables:
• One full-page print ad and digital ad
• Ready-to-print, high-resolution file + working file (PSD, AI, etc.)
Optional: Social media-optimized version or short motion-graphic variation (if designer offers it)
Inspiration & Visual Style Suggestions:
• Think Velvet Voyager, Brimley Hart Wanderer, Seven Lanterns, or Oriel Retreats ad styles
• Large, emotive imagery with elegant typography
• Clean layout that speaks luxury, clarity, and trust
Copy Direction (draft):
For those who’ve explored the world—and crave something beyond the ordinary.
Each journey is a masterfully curated experience, rich in detail, seamless in execution, and unforgettable in every way.
Founded in 1997, Tidewell Journeys is a unique travel company specializing in cruising, all-inclusive luxury properties, and tours world-wide for individuals, groups, and incentives.
We offer an exceptional range of services designed to ensure every journey is flawlessly executed and truly unforgettable.
Let us help you plan your next extraordinary adventure.
Note: You may refine the copy slightly based on layout or format needs.
Other Resources for References:
1. Website - www.tidewelljourneys.example

```html
<!DOCTYPE html>
<html lang="en">
<head>
<meta charset="utf-8">
<title>Tidewell Journeys – Full Page Ad</title>
<link rel="stylesheet" href="https://fonts.googleapis.com/css2?family=Fraunces:wght@900&family=Poppins:wght@600;700&family=Yellowtail&family=Montserrat:wght@800&family=Roboto:wght@500;700&family=Open+Sans:ital@1&family=Roboto+Slab:wght@500;700&display=swap">
<style>
  :root {
    --backdrop: #2b2b2b;
    --sky-deep: #2f9ad8;
    --sky: #45b0e6;
    --cloud: #cfeaf8;
    --sea-deep: #0f5fb0;
    --sea: #1f86d0;
    --lagoon: #3fb6d8;
    --sand: #e9dcc4;
    --linen: #f4f1ea;
    --cream: #f6f3ec;
    --ink: #111111;
    --highlight: #fff200;
    --orange: #f39332;
    --navy: #1c4f8a;
    --wave-blue: #5a9fdb;
    --wave-light: #a8dcf3;
    --leaf: #d7e795;
    --frame: #eef0f2;
  }
  * { margin: 0; padding: 0; box-sizing: border-box; }
  html, body { width: 953px; height: 1200px; overflow: hidden; background: var(--backdrop); }
  .ad {
    position: absolute; left: 21px; top: 13px;
    width: 910px; height: 1174px;
    background: var(--cream); overflow: hidden;
  }
  .hero-photo {
    position: absolute; left: 0; top: 0; width: 910px; height: 815px;
    background:
      radial-gradient(ellipse 300px 420px at 690px 430px, rgba(250,250,250,0.85) 0%, rgba(240,244,247,0.6) 45%, rgba(240,244,247,0) 75%),
      radial-gradient(ellipse 140px 260px at 860px 520px, rgba(230,236,242,0.8) 0%, rgba(230,236,242,0) 80%),
      radial-gradient(ellipse 260px 90px at 180px 130px, rgba(207,234,248,0.7) 0%, rgba(207,234,248,0) 80%),
      radial-gradient(ellipse 200px 70px at 240px 330px, rgba(207,234,248,0.6) 0%, rgba(207,234,248,0) 80%),
      linear-gradient(180deg, var(--sky-deep) 0%, var(--sky) 22%, #7cc8ef 42%, var(--sky) 54%, var(--sea-deep) 57%, var(--sea) 62%, var(--lagoon) 68%, #8fcfe0 71%, var(--sand) 75%, var(--linen) 92%, var(--cream) 100%);
  }
  .headline { position: absolute; left: 44px; top: 46px; font-family: "Fraunces", serif; font-weight: 900; line-height: 1; }
  .headline .lead { display: block; font-size: 44px; letter-spacing: -1px; color: #fff; -webkit-text-stroke: 2px var(--ink); paint-order: stroke fill; }
  .headline .big { display: block; margin-top: 6px; font-size: 66px; letter-spacing: -2px; color: var(--ink); -webkit-text-stroke: 6px var(--highlight); paint-order: stroke fill; }
  .subhead { position: absolute; left: 44px; top: 192px; font-family: "Poppins", sans-serif; color: var(--ink); line-height: 1.3; }
  .subhead .line1 { display: block; font-size: 26px; font-weight: 600; }
  .subhead .line2 { display: block; font-size: 30px; font-weight: 700; }
  .destinations { position: absolute; left: 47px; top: 557px; width: 825px; height: 245px; }
  .destination { position: absolute; top: 0; width: 257px; height: 245px; background: var(--frame); padding: 7px; }
  .destination:nth-child(1) { left: 0; }
  .destination:nth-child(2) { left: 275px; }
  .destination:nth-child(3) { left: 550px; }
  .destination .photo { width: 100%; height: 100%; }
  .photo-cruise { background: linear-gradient(180deg, #5fb1e3 0%, #8cc4e0 18%, #5d9a4e 32%, #7fae5a 42%, #f2f4f6 52%, #e5e9ee 60%, #1f8cc8 66%, #137ab8 85%, #0f68a4 100%); }
  .photo-desert {
    background:
      radial-gradient(circle 40px at 190px 90px, #fff6cf 0%, rgba(255,220,120,0.8) 40%, rgba(255,200,100,0) 100%),
      linear-gradient(180deg, #f5e3a8 0%, #f1bd63 30%, #c9955a 50%, #d7a464 70%, #c08a52 100%);
  }
  .photo-city {
    background:
      radial-gradient(ellipse 120px 50px at 60px 30px, rgba(255,220,150,0.9) 0%, rgba(255,220,150,0) 100%),
      linear-gradient(180deg, #4f86c6 0%, #e8b56a 25%, #d98d5a 45%, #b9845e 60%, #5f8a4a 78%, #e5c04e 100%);
  }
  .script {
    position: absolute; left: 92px; top: 470px;
    font-family: "Yellowtail", cursive; font-size: 48px; line-height: 1; color: var(--ink);
    transform: rotate(-10deg); transform-origin: center;
    -webkit-text-stroke: 4px #fff; paint-order: stroke fill; z-index: 3;
  }
  .cta-tag {
    position: absolute; left: 66px; top: 518px; width: 330px; height: 125px;
    background: var(--orange); border-radius: 18px; transform: rotate(-10deg);
    display: flex; align-items: center; justify-content: center; text-align: center;
    font-family: "Montserrat", sans-serif; font-weight: 800; font-size: 30px; line-height: 1.05; color: #fff;
    z-index: 2;
  }
  .waves { position: absolute; left: 0; top: 0; width: 910px; height: 1174px; }
  .intro { position: absolute; left: 51px; top: 815px; font-family: "Roboto", sans-serif; font-weight: 700; font-size: 23.5px; line-height: 1.22; color: var(--navy); }
  .founded { position: absolute; left: 51px; top: 885px; font-family: "Open Sans", sans-serif; font-style: italic; font-size: 13.3px; line-height: 1.5; color: #333; }
  .offer { position: absolute; left: 99px; top: 968px; width: 270px; text-align: center; font-family: "Roboto Slab", serif; color: var(--navy); }
  .offer h2 { font-size: 30px; font-weight: 700; line-height: 1.15; }
  .offer p { font-size: 17.5px; font-weight: 500; line-height: 1.27; }
  .brand { position: absolute; left: 458px; top: 976px; display: flex; align-items: center; gap: 12px; font-family: "Roboto", sans-serif; font-weight: 500; font-size: 40px; line-height: 1; color: var(--navy); }
  .brand .dot { width: 46px; height: 46px; border-radius: 50%; background: var(--navy); flex: none; }
</style>
</head>
<body>
<main class="ad">
  <div class="hero-photo" role="img" aria-label="Family in white sun hats sitting on a beach, arms raised toward a turquoise sea under palm fronds"></div>

  <h1 class="headline">
    <span class="lead">For those who’ve</span>
    <span class="big">explored the world</span>
  </h1>
  <p class="subhead">
    <span class="line1">and crave something</span>
    <span class="line2">beyond the ordinary</span>
  </p>

  <div class="destinations">
    <figure class="destination"><div class="photo photo-cruise" role="img" aria-label="Cruise ship docked in a green tropical harbour"></div></figure>
    <figure class="destination"><div class="photo photo-desert" role="img" aria-label="Camel resting before desert pyramids at sunset"></div></figure>
    <figure class="destination"><div class="photo photo-city" role="img" aria-label="Colourful mosaic park overlooking a Mediterranean city"></div></figure>
  </div>

  <p class="script">Let us help you</p>
  <div class="cta-tag">Plan your next<br>Extraordinary<br>Adventure</div>

  <svg class="waves" viewBox="0 0 910 1174" aria-hidden="true">
    <defs>
      <linearGradient id="crest" x1="0" y1="0" x2="1" y2="0">
        <stop offset="0" stop-color="#ffffff" stop-opacity="0"/>
        <stop offset="0.6" stop-color="#dcecf7"/>
        <stop offset="1" stop-color="#ffffff"/>
      </linearGradient>
    </defs>
    <path d="M0 895 C30 1010 90 1100 230 1120 C400 1140 560 1075 700 1070 C800 1068 860 1110 910 1150 L910 1174 L0 1174 Z" fill="var(--wave-light)"/>
    <path d="M500 1080 C620 1050 760 1050 850 1100 C880 1120 900 1140 910 1160 L910 1174 L700 1174 Z" fill="url(#crest)"/>
    <path d="M150 1040 C150 985 215 950 290 955 C350 940 410 950 430 990 C470 1015 470 1075 420 1100 C360 1125 250 1130 180 1110 C140 1095 140 1065 150 1040 Z" fill="var(--leaf)"/>
    <path d="M0 935 C25 1060 110 1140 290 1148 C460 1156 590 1095 720 1095 C800 1095 860 1130 900 1174 L0 1174 Z" fill="var(--wave-blue)"/>
  </svg>

  <p class="intro">Each journey is a masterfully curated experience, rich in detail,<br>seamless in execution, and unforgettable in every way.</p>
  <p class="founded">Founded in 1997, Tidewell Journeys is a unique travel company specializing in cruising,<br>all-inclusive luxury properties, and tours world-wide for individuals, groups, and incentives.</p>

  <div class="offer">
    <h2>We offer</h2>
    <p>an exceptional range of services designed to ensure every journey is flawlessly executed and truly unforgettable.</p>
  </div>

  <div class="brand"><span class="dot"></span>Tidewell Journeys</div>
</main>
</body>
</html>
```